Web Design Project

We need a web design company for a company based in London. We are an online minicab booking service that produces real time quotes on cab journey for consumers. Our colours are currently red and yellow, but do not need to stay that way; it's open to interpretation. Please avoid yellow and black as a colour combination. Our current site is: www.ridelark.co.uk We are looking for a new site to be user-friendly and easy to use, but more polished and professional looking, without using it usability and simplicity. We need to keep the booking capability on each page and it needs to draw in the user's eye. We need a site that is reliable and easy to use, but also fun.

Main objective: keep it simple, like it is now, but polish it up some. Also, we need to be able to add more content to it. And, we will also be adding a login capability for return users.

Target Market(s)

Internet-savvy people aged 18 and older.

Industry/Entity Type

It Company

Requirements
Must have
• Must have the booking widget. However, it doesn't have to be as large as it is now. We are actually thinking to split it over two pages. We will add a few options to the booking widget, such as another via option. The booking widget must be the most noticeable feature on the page. Sans serif font, please.
Should not have
• Should not be too busy and distracting. Please do not use any images of traditional taxis, ie. black cabs from London or yellow cabs from NYC. Our cars do not resemble these and our business cannot be associated with these images.

```html
<!DOCTYPE html>
<html lang="en">
<head>
<meta charset="utf-8">
<title>Ridelark – Order your cab online</title>
<link rel="stylesheet" href="https://fonts.googleapis.com/css2?family=Anton&family=Open+Sans:ital,wght@0,400;0,600;1,400&display=swap">
<style>
:root{
  --blue:#0a9af2;
  --blue-dark:#0670c0;
  --red:#f5160c;
  --green-dark:#6aa21c;
  --panel-top:#c7e6f8;
  --panel-bottom:#eef8fd;
  --ink:#1e1e1e;
  --muted:#8a8a8a;
  --field-border:#c9d4dc;
  --white:#ffffff;
}
*{box-sizing:border-box;margin:0;padding:0}
html,body{width:1200px;height:866px;overflow:hidden}
body{position:relative;background:#fbfaf7;font-family:"Open Sans",sans-serif;color:var(--ink)}

.site-header{position:absolute;left:0;top:0;width:1200px;height:245px;background:linear-gradient(#ffffff,#f4f8fb)}
.brand{position:absolute;left:56px;top:34px;display:flex;align-items:center;gap:12px}
.brand-dot{width:18px;height:18px;border-radius:50%;background:var(--blue)}
.brand-name{font-weight:600;font-size:40px;color:var(--blue);line-height:1}
.brand-tag{position:absolute;left:86px;top:80px;font-size:20px;color:#1b2a4a}
.booking-line{position:absolute;left:806px;top:24px;width:349px;height:42px;border-radius:8px;border:1px solid #5c8f1a;background:linear-gradient(#c2e36a,#92c73a);display:flex;align-items:center;justify-content:center;gap:14px;color:#25340a}
.booking-line .label{font-size:18px}
.booking-line .number{font-size:25px;letter-spacing:.5px}
.headline{position:absolute;left:48px;top:148px;font-family:"Anton",sans-serif;font-size:52px;color:var(--red);letter-spacing:.5px;text-shadow:1px 2px 0 #7a0a05}
.skyline{position:absolute;left:578px;top:89px;width:622px;height:156px;background:linear-gradient(90deg,rgba(255,255,255,0),#8fcbf0 35%,#2f8fd6 70%,#bfe2f7)}

.main-nav{position:absolute;left:0;top:245px;width:1200px;height:49px;background:linear-gradient(var(--blue),#0889e0);display:flex;border-bottom:1px solid #0568ad}
.main-nav a{display:flex;align-items:center;justify-content:center;height:49px;color:var(--white);text-decoration:none;font-size:17px;border-right:1px solid rgba(255,255,255,.55)}
.main-nav a:last-child{border-right:0}
.main-nav a.active{background:var(--red)}

.content{position:absolute;left:46px;top:314px;width:703px}
.content h1{font-weight:400;font-size:31px;color:#333;padding-bottom:10px;border-bottom:1px dotted #777}
.content p{font-size:15px;line-height:20px;color:#222}
.content .intro{margin-top:15px}
.content p + p{margin-top:20px}

.promo{position:absolute;top:640px;width:338px;height:112px;border-radius:8px;overflow:hidden;display:flex;box-shadow:0 6px 6px -4px rgba(0,0,0,.25)}
.promo.driver{left:44px}
.promo.rider{left:414px}
.promo-photo{width:180px;height:112px}
.driver .promo-photo{background:linear-gradient(120deg,#2b2b2b,#8d8d8d 55%,#d8d8d8)}
.rider .promo-photo{background:linear-gradient(120deg,#f2f2f2,#b8414a 55%,#3a2a2a)}
.promo-body{flex:1;background:linear-gradient(var(--blue),#0688de);text-align:right;padding:6px 10px 0 0;color:var(--white);font-size:21px;line-height:22px}
.join-btn{display:block;margin:12px 0 0 18px;width:114px;height:38px;border-radius:10px;background:linear-gradient(#8fe3ff,#1cb3f0);border:2px solid #d9f5ff;color:#07223a;font-size:18px;line-height:34px;text-align:center}

.booking-panel{position:absolute;left:774px;top:294px;width:382px;height:460px;background:linear-gradient(var(--panel-top),var(--panel-bottom));border:1px solid #cdd9e0;border-top:0;border-radius:0 0 22px 22px;box-shadow:0 5px 0 #555,0 8px 10px rgba(0,0,0,.25)}
.booking-panel h2{position:absolute;left:20px;top:12px;font-family:"Anton",sans-serif;font-weight:400;font-size:38px;color:var(--red);text-shadow:1px 1px 0 #7a0a05}
.field{position:absolute;left:20px;height:31px;border:1px solid var(--field-border);background:var(--white);font-style:italic;font-size:13.5px;color:var(--muted);padding:6px 8px;box-shadow:inset 1px 1px 2px rgba(0,0,0,.1)}
.field.wide{width:244px}
.find-btn{position:absolute;left:272px;width:65px;height:30px;background:linear-gradient(#5f9ad6,#2a62a6);border:1px solid #1c4d88;color:var(--white);font-style:italic;font-size:15px;text-align:center;line-height:28px}
.select{position:absolute;height:31px;border:1px solid var(--field-border);background:var(--white);font-style:italic;font-size:13.5px;color:var(--muted);padding:6px 8px}
.select svg{position:absolute;right:4px;top:7px}
.check{position:absolute;display:flex;align-items:center;gap:8px;font-style:italic;font-size:13.5px;color:#333}
.check span.box{width:13px;height:13px;border:1px solid #8a98a3;background:var(--white)}
.group-label{position:absolute;left:22px;top:270px;font-style:italic;font-size:13.5px;color:#333}
.calendar{position:absolute;left:272px;top:185px}
.quote-btn{position:absolute;left:14px;top:392px;width:354px;height:52px;border-radius:14px;border:2px solid var(--green-dark);background:linear-gradient(#b9e25c,#8cc33a);display:flex;align-items:center;justify-content:space-between;padding:0 8px 0 12px;font-size:19px;color:#1d2a08}

.site-footer{position:absolute;left:0;top:787px;width:1200px;height:79px;background:linear-gradient(#2b90d9,#1870bd);border-top:3px solid #7cc3f0;color:var(--white)}
.footer-nav{position:absolute;left:43px;top:20px;display:flex;font-size:12px}
.footer-nav a{color:var(--white);text-decoration:none;padding:0 12px;border-left:1px solid var(--white);line-height:12px}
.footer-nav a:first-child{padding-left:0;border-left:0}
.copyright{position:absolute;left:43px;top:38px;font-size:12px}
.cards-label{position:absolute;right:45px;top:15px;font-size:13px}
.cards{position:absolute;right:61px;top:38px;display:flex;gap:5px}
.cards span{width:39px;height:27px;border-radius:3px;background:#f4f4f4;border:1px solid #c9c9c9}
</style>
</head>
<body>

<header class="site-header">
  <div class="brand"><span class="brand-dot"></span><span class="brand-name">Ridelark.co.uk</span></div>
  <div class="brand-tag">Online Cabs Across London</div>
  <div class="booking-line"><span class="label">Booking Line</span><span class="number">020 7946 0182</span></div>
  <div class="headline">Order your cab online</div>
  <div class="skyline" role="img" aria-label="Blue city skyline of glass office towers"></div>
</header>

<nav class="main-nav">
  <a href="#" style="width:165px">Home</a>
  <a href="#" style="width:191px">Ridelark Miles</a>
  <a href="#" class="active" style="width:151px">Join Us</a>
  <a href="#" style="width:156px">About Us</a>
  <a href="#" style="width:101px">Contact</a>
</nav>

<main class="content">
  <h1>Ridelark Miles</h1>
  <p class="intro">At Ridelark, we guarantee that once you use our service, you won’t be ordering a cab any other way again!<br>Unlike any other taxi booking website, our entire service is built with the customer inmind, saving you time and hassle, offering convenience, quality and value for your money.</p>
  <p>It is extremely importnat to us that we look after our customers and to always remind you of how much we value you, themore journeys you book through Ridelark, the more money you will save!</p>
  <p>So waht are you waiting for? Whether you’re a new customer or regular Ridelarker, book your journey with us today, and get saving!</p>
</main>

<section class="promo driver">
  <div class="promo-photo" role="img" aria-label="Driver's hands on a steering wheel"></div>
  <div class="promo-body">Are you a<br>Taxi Driver?<span class="join-btn">JOIN US</span></div>
</section>
<section class="promo rider">
  <div class="promo-photo" role="img" aria-label="Young woman stepping into a red car"></div>
  <div class="promo-body">Are you a<br>Ridelarker?<span class="join-btn">JOIN US</span></div>
</section>

<aside class="booking-panel">
  <h2>Book A Cab</h2>
  <div class="field wide" style="top:70px">Pick&nbsp; up address or post code</div>
  <div class="find-btn" style="top:70px">Find</div>
  <div class="check" style="left:22px;top:113px"><span class="box"></span>add via address:</div>
  <div class="field wide" style="top:140px">Drop address or post code</div>
  <div class="find-btn" style="top:140px">Find</div>
  <div class="field wide" style="top:186px">Pick&nbsp; up date &amp; time</div>
  <svg class="calendar" width="34" height="32" viewBox="0 0 34 32" aria-hidden="true">
    <rect x="1" y="3" width="32" height="28" rx="2" fill="#fff" stroke="#9aa"/>
    <rect x="1" y="3" width="32" height="9" fill="#8cc63f"/>
    <text x="17" y="27" text-anchor="middle" font-family="Open Sans,sans-serif" font-size="14" font-weight="600" fill="#222">26</text>
  </svg>
  <div class="select" style="left:20px;top:226px;width:138px">just pick me in
    <svg width="16" height="16" viewBox="0 0 16 16"><rect x=".5" y=".5" width="15" height="15" fill="#f2f2f2" stroke="#888"/><path d="M4 6h8l-4 5z" fill="#222"/></svg></div>
  <div class="group-label">Passenger &amp; Bags</div>
  <div class="select" style="left:20px;top:293px;width:82px">Adult
    <svg width="16" height="16" viewBox="0 0 16 16"><rect x=".5" y=".5" width="15" height="15" fill="#f2f2f2" stroke="#888"/><path d="M4 6h8l-4 5z" fill="#222"/></svg></div>
  <div class="select" style="left:110px;top:293px;width:84px">Bags
    <svg width="16" height="16" viewBox="0 0 16 16"><rect x=".5" y=".5" width="15" height="15" fill="#f2f2f2" stroke="#888"/><path d="M4 6h8l-4 5z" fill="#222"/></svg></div>
  <div class="check" style="left:22px;top:340px"><span class="box"></span>Return Journey</div>
  <div class="check" style="left:154px;top:340px"><span class="box"></span>Extras</div>
  <div class="quote-btn">Get Your No Obligation quotes
    <svg width="32" height="32" viewBox="0 0 32 32" aria-hidden="true"><circle cx="16" cy="16" r="14" fill="#243a10" stroke="#d9f0a8" stroke-width="2"/><path d="M10 16h10M16 10l6 6-6 6" stroke="#b9e25c" stroke-width="3" fill="none" stroke-linecap="round" stroke-linejoin="round"/></svg>
  </div>
</aside>

<footer class="site-footer">
  <nav class="footer-nav"><a href="#">Home</a><a href="#">Ridelark Miles</a><a href="#">Join Us</a><a href="#">About Us</a><a href="#">Contact</a></nav>
  <div class="copyright">© 2012, All Rights Reserved, www.ridelark.co.uk</div>
  <div class="cards-label">we receive following cards</div>
  <div class="cards"><span></span><span></span><span></span></div>
</footer>

</body>
</html>
```